Web design for business website

I need a web design for a business website for one of our clients who is specialized in alarm management software. I would like you to design 3 web pages, one for each of the 3 pages. You need to process the corporate identity of our client to the web design. This means the colors of the logo (red and black) should definitely show up on all of the 3 pages. Find the logo file for the logo of our customer. To increase readability I suggest you use a white/light background. All suggestions are welcome.

Please kindly download atttached Webdesign.zip and read the project brief first. The project brief refers to all other files of the zip file. Your design must have exactly the same structure as the wireframes.
Updates

Target Market(s)

B2B, Alarm management

Industry/Entity Type

Business

Number of Pages Required

3 page

Requirements
Must have
• The web design must have exactly the same structure as the wireframes and needs to contain the colors of the company logo.

```html
<!DOCTYPE html>
<html lang="en">
<head>
<meta charset="utf-8">
<title>Valoris – Real-time reasoning solutions</title>
<link href="https://fonts.googleapis.com/css2?family=Open+Sans:wght@400;600;700&display=swap" rel="stylesheet">
<style>
:root{
  --accent:#e8461a;
  --ink:#222;
  --muted:#666;
  --topbar:#111;
  --nav:#1b1a3a;
  --light:#f5f5f5;
  --footer:#151515;
  --footer-text:#5e5e5e;
  --grey-btn:#cfcfcf;
}
*{margin:0;padding:0;box-sizing:border-box}
html,body{width:689px;height:1200px;overflow:hidden}
body{font-family:"Open Sans",Arial,sans-serif;color:var(--ink);background:#fff;position:relative}
.abs{position:absolute}
/* top bar */
.topbar{left:0;top:0;width:689px;height:19px;background:var(--topbar);color:#aaa;font-size:7px}
.topbar .phone{left:56px;top:5px;display:flex;gap:5px;align-items:center}
.topbar .lang{left:439px;top:5px}
.topbar .lang-btn{left:495px;top:4px;width:14px;height:12px;background:var(--accent)}
.topbar .lang-val{left:512px;top:4px;width:33px;height:12px;background:#2a2a2a;color:#999;text-align:center;line-height:12px;font-size:7px}
.topbar .search{left:550px;top:4px;width:66px;height:12px;background:#2a2a2a;color:#777;font-size:5.5px;line-height:12px;padding-left:9px}
.topbar .search-btn{left:616px;top:4px;width:17px;height:12px;background:var(--accent)}
/* header */
.header{left:0;top:19px;width:689px;height:50px;background:#fff}
.brand{left:56px;top:31px;display:flex;align-items:center;gap:6px}
.brand .dot{width:25px;height:25px;border-radius:50%;background:var(--accent)}
.brand .name{font-weight:700;font-size:19px;letter-spacing:1.5px;line-height:19px;color:var(--ink)}
.brand .tag{font-size:5.5px;color:#444;margin-top:1px}
.hbtn{top:32px;height:24px;font-size:6px;display:flex;align-items:center;gap:9px;padding:0 9px}
.hbtn.account{left:415px;width:70px;background:var(--accent);color:#fff}
.hbtn.login{left:489px;width:69px;background:#d4d4d4;color:#666}
.hbtn.signup{left:563px;width:69px;background:#d4d4d4;color:#666}
.hbtn .sep{width:1px;height:14px;background:rgba(255,255,255,.5)}
.hbtn.login .sep,.hbtn.signup .sep{background:#aaa}
/* nav */
.nav{left:0;top:69px;width:689px;height:25px;background:var(--nav)}
.nav ul{list-style:none;display:flex;position:absolute;left:56px;top:0}
.nav li{color:#fff;font-size:6.5px;font-weight:600;height:25px;line-height:25px;padding:0 14px;margin-right:7px}
.nav li.active{background:var(--accent);width:50px;text-align:center;padding:0}
/* hero */
.hero{left:0;top:94px;width:689px;height:245px;background:linear-gradient(180deg,#8a8878 0%,#d9b278 32%,#a49a7a 55%,#506a3a 75%,#3b4a2a 100%)}
.hero-box{left:190px;top:146px;width:309px;height:141px;background:rgba(255,255,255,.75);padding:17px 22px}
.hero-box .hello{font-size:10px;color:#222;line-height:12px}
.hero-box .big{display:flex;align-items:baseline;gap:6px}
.hero-box .big b{color:var(--accent);font-size:28px;font-weight:600;line-height:30px}
.hero-box .big span{font-size:8.5px;color:#333}
.hero-box p{font-size:5.5px;color:#444;line-height:8.5px;width:240px;margin-top:4px}
.btn{background:var(--accent);color:#fff;font-size:6px;font-weight:600;text-align:center;box-shadow:0 2px 0 #b3350f}
.hero-box .btn{margin-top:10px;width:78px;height:24px;line-height:24px}
.arrow{top:194px;width:29px;height:29px;display:flex;align-items:center;justify-content:center}
.arrow.prev{left:27px;background:#eee}
.arrow.next{left:632px;background:var(--accent)}
/* welcome */
.welcome{left:0;top:339px;width:689px;height:103px;display:flex;align-items:center;justify-content:center;gap:5px}
.welcome .w{font-size:12px}
.welcome b{font-size:28px;color:var(--accent);font-weight:600}
.welcome .t{font-size:8.5px;color:#333;margin-top:6px}
/* about */
.about{left:0;top:442px;width:689px;height:246px;background:var(--light)}
.about h2{position:absolute;left:57px;top:36px;font-size:17px;color:var(--accent);font-weight:600}
.about p{position:absolute;left:57px;top:68px;width:326px;font-size:6.3px;line-height:9.8px;color:var(--muted)}
.about .btn{position:absolute;left:57px;top:174px;width:79px;height:24px;line-height:24px}
.monitor{left:413px;top:482px}
/* clients */
.clients-head{left:0;top:722px;width:689px;text-align:center}
.clients-head h3{display:inline-block;font-size:13.5px;color:var(--accent);font-weight:600;padding:0 37px 4px;border-bottom:1px solid #bbb}
.clients-head p{font-size:8px;color:#666;margin-top:7px}
.logos{left:0;top:788px;width:689px;height:50px;border-top:1px solid #ddd;border-bottom:1px solid #ddd;display:flex;align-items:center;justify-content:space-around;padding:0 60px}
.logos span{font-size:9px;font-weight:700;color:#444}
/* follow band */
.band{left:0;top:881px;width:689px;height:123px;background:linear-gradient(180deg,#222 0%,#2e2a24 55%,#15140f 100%)}
.band h4{position:absolute;top:33px;font-size:16px;color:var(--accent);font-weight:400}
.socials{left:56px;top:945px;display:flex;gap:5px}
.socials div{width:25px;height:25px;background:#8a8a8a}
.socials div:first-child{background:#3b5897}
.subscribe{left:253px;top:945px;width:379px;height:25px;border:1px solid #fff;display:flex}
.subscribe .field{flex:1;background:#111;color:#ddd;font-size:6.5px;line-height:23px;padding-left:14px}
.subscribe .go{width:68px;background:#fff;color:var(--accent);font-size:6.5px;font-weight:700;text-align:center;line-height:23px}
/* footer */
.footer{left:0;top:1004px;width:689px;height:166px;background:var(--footer)}
.fcol{top:1042px;font-size:6.5px;color:var(--footer-text);line-height:11px}
.fcol h5{font-size:8.5px;font-weight:400;color:#3c3c3c;margin-bottom:10px}
.fcol .hi{color:var(--accent)}
.fcol .row{display:flex;gap:8px;align-items:center;margin-bottom:5px}
.bottom{left:0;top:1170px;width:689px;height:30px;background:var(--footer);border-top:1px solid #262626;text-align:center;font-size:5.5px;color:#444;line-height:29px}
.bottom b{color:var(--accent);font-weight:600}
</style>
</head>
<body>

<div class="abs topbar">
  <div class="abs phone"><svg width="6" height="6" viewBox="0 0 10 10"><path d="M2 0l2 2-1 2 3 3 2-1 2 2-2 2C4 10 0 6 0 2z" fill="#aaa"/></svg>+31 (0)20 555 0147</div>
  <div class="abs lang">Selecte Language :</div>
  <div class="abs lang-btn"><svg width="14" height="12"><path d="M5 5h4l-2 2z" fill="#fff"/></svg></div>
  <div class="abs lang-val">ENG</div>
  <div class="abs search">Search here...</div>
  <div class="abs search-btn"><svg width="17" height="12"><circle cx="8" cy="5.5" r="2.5" stroke="#fff" fill="none"/><path d="M10 7.5l2 2" stroke="#fff"/></svg></div>
</div>

<div class="abs header"></div>
<div class="abs brand"><div class="dot"></div><div><div class="name">VALORIS</div><div class="tag">Real-time reasoning solutions</div></div></div>
<div class="abs hbtn account"><svg width="7" height="7" viewBox="0 0 10 10"><circle cx="5" cy="3" r="2.5" fill="#fff"/><path d="M0 10c0-4 10-4 10 0z" fill="#fff"/></svg><span class="sep"></span>ACCOUNT</div>
<div class="abs hbtn login"><svg width="7" height="7" viewBox="0 0 10 10"><rect x="1" y="4" width="6" height="5" fill="#555"/><path d="M5 4V2a2 2 0 014 0" stroke="#555" fill="none"/></svg><span class="sep"></span>LOG IN</div>
<div class="abs hbtn signup"><svg width="7" height="7" viewBox="0 0 10 10"><path d="M0 4h5V1l4 4-4 4V6H0z" fill="#555"/></svg><span class="sep"></span>SIGN UP</div>

<nav class="abs nav"><ul><li class="active">HOME</li><li>INDUSTRY</li><li>TELECOM</li><li>POWER</li><li>UTILITIES</li><li>INFRA</li><li>STORE</li></ul></nav>

<div class="abs hero" role="img" aria-label="Photo of an industrial refinery beside a marsh under a sunset sky"></div>
<div class="abs arrow prev"><svg width="6" height="8"><path d="M5 0L1 4l4 4" stroke="var(--accent)" stroke-width="1.6" fill="none"/></svg></div>
<div class="abs arrow next"><svg width="6" height="8"><path d="M1 0l4 4-4 4" stroke="#fff" stroke-width="1.6" fill="none"/></svg></div>
<div class="abs hero-box">
  <div class="hello">HELLO WE ARE</div>
  <div class="big"><b>VALORIS</b><span>Real-time reasoning solutions</span></div>
  <p>Companies have invested to get data out of processes. New technologies have been developed to get real-time data out of the harshest places, like oil-well drill heads or the Great Barrier Riff.</p>
  <div class="btn">READ MORE</div>
</div>

<section class="abs welcome"><span class="w">WELCOME TO</span><b>VALORIS</b><span class="t">Real-time reasoning solutions</span></section>

<section class="abs about">
  <h2>ABOUT US</h2>
  <p>Companies have invested to get data out of processes. New technologies have been developed to get real-time data out of the harshest places, like oil-well drill heads or the Great Barrier Riff. Data in itself means nothing without the context the data is collected in. Example: data from equipment under maintenance does not provide information to operations. Information - data which is valid and meaningful can overwhelm any user without the proper knowledge to interpret this information. Valoris technology enables easy application of such knowledge in a comprehensible – visual – representation and makes hypothetical reasoning with information possible providing meaningful advisories to subscribers when they need it or when it is required that they are made aware of a situation which requires their attention.</p>
  <div class="btn">LEARN MORE</div>
</section>
<svg class="abs monitor" width="219" height="150" viewBox="0 0 219 150">
  <rect x="0" y="0" width="219" height="125" rx="3" fill="#1a1a1a"/>
  <rect x="0" y="108" width="219" height="17" fill="#d6d6d6"/>
  <defs><linearGradient id="city" x1="0" y1="0" x2="0" y2="1"><stop offset="0" stop-color="#e9b46a"/><stop offset="1" stop-color="#7a5a3a"/></linearGradient></defs>
  <rect x="10" y="10" width="199" height="93" fill="url(#city)" role="img" aria-label="Photo of a city highway interchange at sunset"/>
  <path d="M90 125h39l4 18H86z" fill="#cfcfcf"/>
  <ellipse cx="109" cy="146" rx="40" ry="3" fill="#ddd"/>
</svg>

<div class="abs clients-head"><h3>CLIENTS THAT TRUST US</h3><p>Some of our clients that trust us, be shure to be one of them.</p></div>
<div class="abs logos"><span>Norvane</span><span>quarrytech</span><span>Elmfield</span><span>KVT</span><span>Brouwvelt</span><span>Tidewell</span><span>Stranda Oil</span></div>

<section class="abs band" role="img" aria-label="Dim photo of an industrial plant at night">
  <h4 style="left:56px">FOLLOW US ON :</h4>
  <h4 style="left:253px">SUBSCRIBE NOW :</h4>
</section>
<div class="abs socials" aria-label="Social links"><div></div><div></div><div></div><div></div><div></div></div>
<div class="abs subscribe"><div class="field">Enter Your Email Adress</div><div class="go">SUBSCRIBE</div></div>

<footer class="abs footer"></footer>
<div class="abs fcol" style="left:56px"><h5>SOLUTIONS</h5><div class="hi">SAM Alarm Reporting</div><div>SAM Alarm Analysis</div><div>SAM Alarm Expert</div><div>USE</div></div>
<div class="abs fcol" style="left:154px"><h5>INDUSTRIES</h5><div>Industry</div><div>Telecom</div><div>Power</div><div>Utilites</div><div>Infra</div></div>
<div class="abs fcol" style="left:254px"><h5>ABOUT US</h5><div>Company</div><div>Overview</div><div>Leadership</div><div>Partners</div><div>Locations</div></div>
<div class="abs fcol" style="left:352px"><h5>NEWS</h5><div>Product News</div><div>Partner News</div><div>Events</div><div>Press Releases</div><div>Vacancies</div></div>
<div class="abs fcol" style="left:499px"><h5>CONTACT US</h5>
  <div class="row"><svg width="6" height="6" viewBox="0 0 10 10"><path d="M2 0l2 2-1 2 3 3 2-1 2 2-2 2C4 10 0 6 0 2z" fill="#5e5e5e"/></svg>+31 (0)20 555 0147</div>
  <div class="row"><svg width="7" height="5" viewBox="0 0 10 7"><rect width="10" height="7" fill="#5e5e5e"/><path d="M0 0l5 4 5-4" stroke="#151515" fill="none"/></svg>info@valoris.example</div>
  <div class="row"><svg width="5" height="7" viewBox="0 0 6 9"><path d="M3 9L0 4a3 3 0 116 0z" fill="#5e5e5e"/></svg>address Valoris Leiden</div>
</div>
<div class="abs bottom">Copyright © 2105 <b>VALORIS</b>. All Rights Reserved.</div>

</body>
</html>
```